Chiropractic Flyers to be made more up to date

I have used this series of flyers for my own practice. I would like the graphics to be brought up to date and the name of the doctor and the practice, the address, phone number and date to be removed and a blank box inserted in one place on the flyer that other chiropractors could use to personalize the flyers for their practice. On some of the flyers, this information is in several places. I'd like to have it all in one space so that it would be easy for the doctor to add it in their practice. They all need to be bright and colorful with catchy graphics.

Industry/Entity Type

Doctor

```html
<!DOCTYPE html>
<html lang="en">
<head>
<meta charset="UTF-8">
<title>Backpack Safety Demonstration Flyer</title>
<link rel="stylesheet" href="https://fonts.googleapis.com/css2?family=Bebas+Neue&family=Oswald:wght@500;600&family=Arimo:wght@400;700&display=swap">
<style>
  :root {
    --stage: #1b1b1b;
    --paper: #ffffff;
    --title-top: #ffd21a;
    --title-bottom: #f08a00;
    --ink: #1a1a1a;
    --band: rgba(40, 40, 40, 0.62);
    --bullet-text: #ffd21a;
    --tick: #ffffff;
    --sticker-top: #ffe03a;
    --sticker-bottom: #ffb000;
    --sticker-text: #e0151b;
    --swoosh: #8c1a7c;
    --photo-warm: #8a6a44;
    --photo-dark: #4a3a2c;
    --photo-light: #c9c2b6;
    --rule: #222222;
  }
  * { box-sizing: border-box; margin: 0; padding: 0; }
  html, body {
    width: 1200px; height: 900px; overflow: hidden;
    background: var(--stage);
  }
  .canvas {
    width: 1200px; height: 900px;
    display: flex; align-items: center; justify-content: center;
  }
  .flyer {
    position: relative;
    width: 600px; height: 860px;
    background: var(--paper);
    overflow: hidden;
    box-shadow: 0 10px 40px rgba(0,0,0,0.6);
  }
  .flyer-art {
    position: absolute; inset: 0;
    width: 600px; height: 860px;
  }
  .title {
    position: absolute; top: 14px; left: 0; right: 0;
    text-align: center;
    white-space: nowrap;
    font-family: "Bebas Neue", sans-serif;
    font-weight: 400;
    font-size: 90px; line-height: 1;
    letter-spacing: 0.5px;
    background: linear-gradient(180deg, var(--title-top) 20%, var(--title-bottom) 95%);
    -webkit-background-clip: text; background-clip: text;
    color: transparent;
  }
  .subtitle {
    position: absolute; top: 104px; left: 0; right: 0;
    text-align: center;
    white-space: nowrap;
    font-family: "Oswald", sans-serif; font-weight: 500;
    font-size: 40px; line-height: 1.1; letter-spacing: 13px;
    color: var(--ink);
    padding-left: 13px;
  }
  .benefits {
    position: absolute; top: 388px; left: 0; right: 0;
    height: 150px;
    background: var(--band);
    padding: 14px 14px 0 14px;
    list-style: none;
    font-family: "Arimo", sans-serif;
    font-size: 17px; line-height: 1.3;
    color: var(--bullet-text);
  }
  .benefits li {
    position: relative;
    padding-left: 26px;
    margin-bottom: 12px;
  }
  .benefits .tick {
    position: absolute; left: 0; top: 0;
    width: 20px; height: 20px;
  }
  .sticker {
    position: absolute; left: 36px; top: 660px;
    width: 222px; height: 122px;
    transform: rotate(-14deg);
    background: linear-gradient(180deg, var(--sticker-top), var(--sticker-bottom));
    box-shadow: 2px 4px 8px rgba(0,0,0,0.35);
    display: flex; flex-direction: column; align-items: center; justify-content: center;
    font-family: "Oswald", sans-serif; font-weight: 600;
    color: var(--sticker-text);
    line-height: 1;
    text-transform: uppercase;
  }
  .sticker .big { font-size: 48px; }
  .sticker .small { font-size: 30px; margin-top: 2px; }
  .audience {
    position: absolute; right: 30px; top: 740px;
    width: 250px;
    text-align: center;
    font-family: "Oswald", sans-serif; font-weight: 500;
    font-size: 21px; letter-spacing: 0.5px;
    color: var(--ink);
  }
  .audience .divider { display: block; margin: 4px auto 0; }
  .practice-details {
    position: absolute; right: 30px; top: 792px;
    width: 370px; height: 60px;
    display: flex; flex-direction: column; justify-content: space-between;
  }
  .practice-details span {
    display: block; height: 2px; background: var(--rule);
  }
</style>
</head>
<body>
<main class="canvas">
  <article class="flyer">
    <svg class="flyer-art" viewBox="0 0 600 860">
      <defs>
        <linearGradient id="photoTone" x1="0" y1="0" x2="0" y2="1">
          <stop offset="0" stop-color="#c9c2b6"/>
          <stop offset="0.35" stop-color="#8a6a44"/>
          <stop offset="0.75" stop-color="#4a3a2c"/>
          <stop offset="1" stop-color="#c9c2b6"/>
        </linearGradient>
        <linearGradient id="photoFade" x1="0" y1="0" x2="0" y2="1">
          <stop offset="0" stop-color="#ffffff" stop-opacity="1"/>
          <stop offset="0.12" stop-color="#ffffff" stop-opacity="0"/>
        </linearGradient>
      </defs>
      <g role="img" aria-label="Photo of a student in a plaid shirt wearing a brown canvas backpack, seen from behind on a city street">
        <path d="M0 180 H600 V545 C520 640 300 660 0 800 Z" fill="url(#photoTone)"/>
        <path d="M0 180 H600 V545 C520 640 300 660 0 800 Z" fill="url(#photoFade)"/>
      </g>
      <path class="swoosh" d="M600 545 C520 640 300 660 0 800" fill="none" stroke="#8c1a7c" stroke-width="2.5"/>
    </svg>

    <h1 class="title">Backpack Safety</h1>
    <p class="subtitle">DEMONSTRATION</p>

    <ul class="benefits">
      <li><svg class="tick" viewBox="0 0 20 20"><path d="M2 11 L7 16 L18 3" fill="none" stroke="#ffffff" stroke-width="3"/></svg>Learn how your posture can effect your attiude and self-esteem.</li>
      <li><svg class="tick" viewBox="0 0 20 20"><path d="M2 11 L7 16 L18 3" fill="none" stroke="#ffffff" stroke-width="3"/></svg>Learn the posture of a “ WINNER ” &amp; how to avoid the posture of a “LOSER.”</li>
      <li><svg class="tick" viewBox="0 0 20 20"><path d="M2 11 L7 16 L18 3" fill="none" stroke="#ffffff" stroke-width="3"/></svg>Learn poper backpack safety to stand up for success.</li>
    </ul>

    <div class="sticker">
      <span class="big">Stand Up</span>
      <span class="small">For Success!</span>
    </div>

    <div class="audience">
      PARENTS &amp; FACULTY INVITED
      <svg class="divider" width="170" height="10" viewBox="0 0 170 10">
        <line x1="0" y1="5" x2="170" y2="5" stroke="#222222" stroke-width="1"/>
        <path d="M70 5 L85 1 L100 5 L85 9 Z" fill="#222222"/>
      </svg>
    </div>

    <div class="practice-details" aria-label="Space for practice name, address, phone and date">
      <span></span><span></span><span></span>
    </div>
  </article>
</main>
</body>
</html>
```